Financial investment & advisory business needs a powerpoint design

We need a powerpoint design incorporating the logo (and colours) and relating to the business card design we already have. The company is a boutique financial investment and advisory business called Brimwood Capital Pty Ltd based in Australia. The final design should communicate innovative advice and financial safety and growth. A young, contemporary but experienced, professional business.

Target Market(s)

Companies listed or wishing to list on the Tarrowvale Share Market and Professional and Institutional Investors.

Industry/Entity Type

Finance

Requirements
Must have
• Incorporate the logo and colours. Be similar/relate to the business card design.
Nice to have
Should not have
• Do not deviate from the logo colours.
• Do not use black background or invert the logo.
• Do not deviate from the business card design too much.

```html
<!DOCTYPE html>
<html lang="en">
<head>
<meta charset="utf-8">
<title>Brimwood Capital – Presentation Template</title>
<link href="https://fonts.googleapis.com/css2?family=Open+Sans:wght@400;600;700&display=swap" rel="stylesheet">
<style>
  :root{
    --blue:#3d63b0;
    --blue-light:#5b93d3;
    --grey:#8a8a8a;
    --grey-dark:#6f6f6f;
    --grey-mid:#9d9d9d;
    --grey-soft:#b8b8b8;
    --grey-light:#d9d9d9;
    --white:#fff;
    --page:#e9e9e9;
  }
  *{margin:0;padding:0;box-sizing:border-box}
  html,body{width:1200px;height:512px;overflow:hidden;background:var(--page)}
  body{font-family:"Open Sans",Arial,sans-serif;position:relative}
  .slide{position:absolute;width:296px;height:166px;background:var(--white);border:1px solid #cfcfcf;overflow:hidden}
  .slide svg{position:absolute;inset:0;width:100%;height:100%}
  .c1{left:0}.c2{left:301px}.c3{left:602px}.c4{left:903px}
  .r1{top:2px}.r2{top:173px}.r3{top:344px}
  .kicker{position:absolute;left:15px;top:14px;width:22px;height:1.5px;background:var(--blue)}
  .title{position:absolute;left:15px;top:18px;font-size:9px;font-weight:600;color:var(--grey-dark);white-space:nowrap}
  .title b{color:var(--blue);font-weight:700}
  .sub{position:absolute;left:15px;top:31px;font-size:5px;color:var(--grey)}
  .brand{font-family:"Open Sans",Arial,sans-serif;font-weight:600;fill:var(--blue);letter-spacing:.6px}
  .t-tiny{font-size:2.6px;fill:#999}
  .t-label{font-size:3px;font-weight:700;fill:var(--blue)}
  .t-label-w{font-size:3px;font-weight:700;fill:var(--white)}
  .t-foot{font-size:4.2px;font-weight:600;fill:var(--white)}
  .t-num{font-size:3.6px;font-weight:700;fill:var(--white)}
  .t-body{font-size:3.2px;fill:#888}
  .t-big{font-size:13px;font-weight:700;fill:var(--white)}
  .photo-sky{fill:url(#sky)}
</style>
</head>
<body>
<svg width="0" height="0" style="position:absolute">
  <defs>
    <linearGradient id="sky" x1="0" y1="0" x2="0" y2="1">
      <stop offset="0" stop-color="#3e6fb8"/>
      <stop offset=".5" stop-color="#9ab6d8"/>
      <stop offset="1" stop-color="#5d6a78"/>
    </linearGradient>
  </defs>
</svg>

<!-- Cover -->
<div class="slide c1 r1">
  <svg viewBox="0 0 296 166">
    <rect class="photo-sky" width="296" height="166" role="img" aria-label="City skyline photo with cable-stayed bridge"/>
    <polygon points="0,0 148,0 0,28" fill="#fff"/>
    <text class="brand" x="6" y="13" font-size="8">BRIMWOOD CAPITAL</text>
    <polygon points="180,0 296,0 296,166 90,166" fill="var(--blue)" opacity=".82"/>
    <text class="t-big" x="282" y="122" text-anchor="end">Company</text>
    <text class="t-big" x="282" y="141" text-anchor="end">Presentation</text>
  </svg>
</div>

<!-- At glance -->
<div class="slide c2 r1">
  <svg viewBox="0 0 296 166">
    <rect x="148" y="0" width="148" height="150" class="photo-sky" role="img" aria-label="Photo of a glass bubble against a blue cloudy sky"/>
    <text class="t-body" x="15" y="62">Sed ut perspiciatis unde omnis iste natus error sit</text>
    <text class="t-body" x="15" y="67">voluptatem accusantium doloremque laudantium totam</text>
    <text class="t-body" x="15" y="72">rem aperiam eaque ipsa quae ab illo inventore.</text>
    <rect x="15" y="88" width="120" height="24" fill="#7b7b7b"/>
    <text class="t-label-w" x="19" y="96" font-weight="400">Sed ut perspiciatis unde omnis iste natus error</text>
    <text class="t-label-w" x="19" y="101" font-weight="400">accusantium doloremque laudantium totam rem</text>
    <text class="t-label-w" x="19" y="106" font-weight="400">eaque ipsa quae ab illo.</text>
    <text class="t-body" x="15" y="122">Sed ut perspiciatis unde omnis iste natus error sit</text>
    <text class="t-body" x="15" y="127">voluptatem accusantium doloremque laudantium totam</text>
    <text class="t-body" x="15" y="132">rem aperiam eaque ipsa quae ab illo inventore.</text>
    <rect y="150" width="296" height="16" fill="#fff"/>
    <text class="brand" x="5" y="161" font-size="5.5">BRIMWOOD CAPITAL</text>
    <polygon points="82,150 296,150 296,166 70,166" fill="var(--blue)"/>
    <polygon points="270,150 296,150 296,166 258,166" fill="var(--blue-light)"/>
    <text class="t-foot" x="232" y="160" text-anchor="end">© Brimwood Capital 2017</text>
    <text class="t-foot" x="282" y="160">2</text>
  </svg>
  <div class="kicker"></div>
  <div class="title"><b>Brimwood</b> At Glance</div>
  <div class="sub" style="width:120px;line-height:6px">Insert some short and brief explanatory text about title here</div>
</div>

<!-- Principles -->
<div class="slide c3 r1">
  <svg viewBox="0 0 296 166">
    <circle cx="148" cy="90" r="27" fill="var(--blue)"/>
    <circle cx="148" cy="90" r="21" fill="none" stroke="#fff" stroke-width=".8" opacity=".6"/>
    <g fill="var(--grey-dark)">
      <circle cx="104" cy="60" r="5"/><circle cx="95" cy="80" r="5"/><circle cx="95" cy="102" r="5"/><circle cx="104" cy="122" r="5"/>
      <circle cx="192" cy="60" r="5"/><circle cx="201" cy="80" r="5"/><circle cx="201" cy="102" r="5"/><circle cx="192" cy="122" r="5"/>
    </g>
    <g class="t-num" text-anchor="middle" font-size="3px">
      <text x="104" y="61">01</text><text x="95" y="81">03</text><text x="95" y="103">05</text><text x="104" y="123">07</text>
      <text x="192" y="61">02</text><text x="201" y="81">04</text><text x="201" y="103">06</text><text x="192" y="123">08</text>
    </g>
    <g text-anchor="end">
      <text class="t-label" x="95" y="58">LOREM OPTIONS</text><text class="t-tiny" x="95" y="62">Short sample line of text</text>
      <text class="t-label" x="86" y="78">LOREM OPTIONS</text><text class="t-tiny" x="86" y="82">Short sample line of text</text>
      <text class="t-label" x="86" y="100">LOREM OPTIONS</text><text class="t-tiny" x="86" y="104">Short sample line of text</text>
      <text class="t-label" x="95" y="120">LOREM OPTIONS</text><text class="t-tiny" x="95" y="124">Short sample line of text</text>
    </g>
    <g>
      <text class="t-label" x="201" y="58">LOREM OPTIONS</text><text class="t-tiny" x="201" y="62">Short sample line of text</text>
      <text class="t-label" x="210" y="78">LOREM OPTIONS</text><text class="t-tiny" x="210" y="82">Short sample line of text</text>
      <text class="t-label" x="210" y="100">LOREM OPTIONS</text><text class="t-tiny" x="210" y="104">Short sample line of text</text>
      <text class="t-label" x="201" y="120">LOREM OPTIONS</text><text class="t-tiny" x="201" y="124">Short sample line of text</text>
    </g>
    <rect y="150" width="296" height="16" fill="#fff"/>
    <text class="brand" x="5" y="161" font-size="5.5">BRIMWOOD CAPITAL</text>
    <polygon points="82,150 296,150 296,166 70,166" fill="var(--blue)"/>
    <polygon points="270,150 296,150 296,166 258,166" fill="var(--blue-light)"/>
    <text class="t-foot" x="232" y="160" text-anchor="end">© Brimwood Capital 2017</text>
    <text class="t-foot" x="282" y="160">3</text>
  </svg>
  <div class="kicker"></div>
  <div class="title"><b>Team/Company</b> Principles</div>
  <div class="sub">Short team principles description</div>
</div>

<!-- History -->
<div class="slide c4 r1">
  <svg viewBox="0 0 296 166">
    <rect x="20" y="92" width="262" height="5" rx="2.5" fill="var(--blue)"/>
    <path d="M148,92 V78 H244 V92" fill="none" stroke="var(--grey)" stroke-width=".6"/>
    <g fill="var(--grey-dark)" stroke="#fff" stroke-width="1">
      <circle cx="47" cy="94.5" r="5"/><circle cx="91" cy="94.5" r="5"/><circle cx="148" cy="94.5" r="5"/><circle cx="196" cy="94.5" r="5"/><circle cx="244" cy="94.5" r="5"/>
    </g>
    <g class="t-label" text-anchor="middle" style="fill:var(--grey-dark)">
      <text x="47" y="106">2010</text><text x="91" y="86">2011</text><text x="148" y="106">2012</text><text x="196" y="86">2013</text><text x="244" y="106">2014</text>
    </g>
    <g text-anchor="middle">
      <text class="t-label" x="47" y="55">ESTABLISHMENT</text><text class="t-tiny" x="47" y="60">Short sample line of text</text><text class="t-tiny" x="47" y="64">about this milestone</text>
      <text class="t-label" x="148" y="55">IT REGISTRATION</text><text class="t-tiny" x="148" y="60">Short sample line of text</text><text class="t-tiny" x="148" y="64">about this milestone</text>
      <text class="t-label" x="258" y="55">TOP BRANDS LIST</text><text class="t-tiny" x="258" y="60">Short sample line of text</text><text class="t-tiny" x="258" y="64">about this milestone</text>
      <text class="t-label" x="196" y="68" style="fill:var(--grey-dark)">$10 BILLION</text><text class="t-label" x="196" y="72" style="fill:var(--grey-dark)">REVENUE</text>
      <text class="t-label" x="91" y="117">REFINEMENT</text><text class="t-tiny" x="91" y="122">Short sample line of text</text><text class="t-tiny" x="91" y="126">about this milestone</text>
      <text class="t-label" x="210" y="117">HOSTING CAPABILITIES</text><text class="t-tiny" x="210" y="122">Short sample line of text</text><text class="t-tiny" x="210" y="126">about this milestone</text>
    </g>
    <rect y="150" width="296" height="16" fill="#fff"/>
    <text class="brand" x="5" y="161" font-size="5.5">BRIMWOOD CAPITAL</text>
    <polygon points="82,150 296,150 296,166 70,166" fill="var(--blue)"/>
    <polygon points="270,150 296,150 296,166 258,166" fill="var(--blue-light)"/>
    <text class="t-foot" x="232" y="160" text-anchor="end">© Brimwood Capital 2017</text>
    <text class="t-foot" x="282" y="160">4</text>
  </svg>
  <div class="kicker"></div>
  <div class="title"><b>Company</b> History</div>
  <div class="sub">Short time line description.</div>
</div>

<!-- Showcase -->
<div class="slide c1 r2">
  <svg viewBox="0 0 296 166">
    <rect x="20" y="48" width="256" height="30" fill="#7b7b7b"/>
    <text class="t-label-w" x="26" y="57">CLIENT: LOREM COMPANY</text>
    <text class="t-label-w" x="26" y="63" font-weight="400">Sed ut perspiciatis unde omnis iste natus error</text>
    <text class="t-label-w" x="26" y="67" font-weight="400">sit voluptatem accusantium doloremque</text>
    <rect x="165" y="55" width="84" height="54" rx="3" fill="#cfd2d6" role="img" aria-label="Laptop mock-up showing the project"/>
    <rect x="170" y="60" width="74" height="45" fill="#fff"/>
    <rect x="158" y="109" width="98" height="4" rx="2" fill="#b6b9bd"/>
    <circle cx="34" cy="88" r="3" fill="var(--blue)"/><circle cx="34" cy="99" r="3" fill="var(--blue)"/>
    <text class="t-tiny" x="40" y="89">Short sample line of text here</text>
    <text class="t-tiny" x="40" y="100">Short sample line of text here</text>
    <line x1="28" y1="110" x2="140" y2="110" stroke="var(--grey-light)" stroke-width=".5"/>
    <text class="t-tiny" x="28" y="117">Sed ut perspiciatis unde omnis iste natus</text>
    <rect y="150" width="296" height="16" fill="#fff"/>
    <text class="brand" x="5" y="161" font-size="5.5">BRIMWOOD CAPITAL</text>
    <polygon points="82,150 296,150 296,166 70,166" fill="var(--blue)"/>
    <polygon points="270,150 296,150 296,166 258,166" fill="var(--blue-light)"/>
    <text class="t-foot" x="232" y="160" text-anchor="end">© Brimwood Capital 2017</text>
    <text class="t-foot" x="282" y="160">5</text>
  </svg>
  <div class="kicker"></div>
  <div class="title"><b>Project/Client</b> Showcase</div>
  <div class="sub">Short project description</div>
</div>

<!-- Section -->
<div class="slide c2 r2">
  <svg viewBox="0 0 296 166">
    <rect class="photo-sky" width="296" height="166" role="img" aria-label="City skyline photo with bridge and towers"/>
    <polygon points="0,0 175,0 0,150" fill="#fff" opacity=".8"/>
    <text class="brand" x="6" y="20" font-size="8">BRIMWOOD CAPITAL</text>
    <polygon points="296,30 296,166 150,166" fill="var(--blue)" opacity=".82"/>
    <text class="t-big" x="286" y="146" text-anchor="end">Section Slide</text>
  </svg>
</div>

<!-- Services -->
<div class="slide c3 r2">
  <svg viewBox="0 0 296 166">
    <g fill="var(--blue)"><circle cx="54" cy="91" r="16"/><circle cx="118" cy="91" r="16"/><circle cx="182" cy="91" r="16"/><circle cx="246" cy="91" r="16"/></g>
    <g fill="none" stroke="#fff" stroke-width="1.2">
      <rect x="47" y="85" width="14" height="9" rx="1"/><line x1="54" y1="94" x2="54" y2="98"/><line x1="50" y1="98" x2="58" y2="98"/>
      <rect x="114" y="83" width="8" height="15" rx="1.5"/>
      <path d="M176,98 L187,85 L190,88 L179,100 Z"/>
      <path d="M238,85 h12 v8 h-7 l-3,3 v-3 h-2 z"/><path d="M244,95 h10 v-7"/>
    </g>
    <g text-anchor="middle" class="t-label" style="fill:var(--grey-dark)">
      <text x="54" y="119">DESIGN &amp; DEV</text>
      <text x="118" y="119">MOBILE APPS</text>
      <text x="182" y="119">COPYWRITING</text>
      <text x="246" y="119">SOCIAL MARKETING</text>
    </g>
    <g stroke="var(--blue)" stroke-width=".6"><line x1="32" y1="122" x2="76" y2="122"/><line x1="96" y1="122" x2="140" y2="122"/><line x1="160" y1="122" x2="204" y2="122"/><line x1="224" y1="122" x2="268" y2="122"/></g>
    <g text-anchor="middle">
      <text class="t-tiny" x="54" y="128">Short sample line of text</text><text class="t-tiny" x="54" y="132">for this service</text>
      <text class="t-tiny" x="118" y="128">Short sample line of text</text><text class="t-tiny" x="118" y="132">for this service</text>
      <text class="t-tiny" x="182" y="128">Short sample line of text</text><text class="t-tiny" x="182" y="132">for this service</text>
      <text class="t-tiny" x="246" y="128">Short sample line of text</text><text class="t-tiny" x="246" y="132">for this service</text>
    </g>
    <rect y="150" width="296" height="16" fill="#fff"/>
    <text class="brand" x="5" y="161" font-size="5.5">BRIMWOOD CAPITAL</text>
    <polygon points="82,150 296,150 296,166 70,166" fill="var(--blue)"/>
    <polygon points="270,150 296,150 296,166 258,166" fill="var(--blue-light)"/>
    <text class="t-foot" x="232" y="160" text-anchor="end">© Brimwood Capital 2017</text>
    <text class="t-foot" x="282" y="160">6</text>
  </svg>
  <div class="kicker"></div>
  <div class="title"><b>Services</b> Show</div>
  <div class="sub">Short services description</div>
</div>

<!-- Revenue -->
<div class="slide c4 r2">
  <svg viewBox="0 0 296 166">
    <text class="t-label" x="20" y="64">LOREM IPSUM TITLE</text>
    <text class="t-tiny" x="20" y="70">Sed ut perspiciatis unde omnis iste natus</text>
    <text class="t-tiny" x="20" y="74">error sit voluptatem accusantium totam</text>
    <text class="t-tiny" x="20" y="78">rem aperiam eaque ipsa quae ab illo</text>
    <text class="t-tiny" x="20" y="82">inventore veritatis et quasi architecto</text>
    <g fill="#9d9d9d" opacity=".85">
      <polygon points="125,135 150,74 175,135"/>
      <polygon points="150,135 176,86 202,135"/>
      <polygon points="230,135 256,86 282,135"/>
      <polygon points="198,135 225,80 252,135"/>
    </g>
    <polygon points="172,135 202,56 232,135" fill="var(--blue)" opacity=".9"/>
    <g text-anchor="middle" font-size="4px" fill="var(--grey-dark)">
      <text x="150" y="70">16.25%</text><text x="176" y="82">14.22%</text><text x="202" y="52" fill="var(--blue)" font-weight="700">18.2%</text><text x="225" y="76">16.1%</text><text x="256" y="82">17.42%</text>
    </g>
    <rect x="125" y="135" width="157" height="5" rx="2.5" fill="var(--blue)"/>
    <g class="t-num" font-size="2.8px" text-anchor="middle">
      <text x="150" y="138.6">2010</text><text x="176" y="138.6">2011</text><text x="202" y="138.6">2012</text><text x="225" y="138.6">2013</text><text x="256" y="138.6">2014</text>
    </g>
    <rect y="150" width="296" height="16" fill="#fff"/>
    <text class="brand" x="5" y="161" font-size="5.5">BRIMWOOD CAPITAL</text>
    <polygon points="82,150 296,150 296,166 70,166" fill="var(--blue)"/>
    <polygon points="270,150 296,150 296,166 258,166" fill="var(--blue-light)"/>
    <text class="t-foot" x="232" y="160" text-anchor="end">© Brimwood Capital 2017</text>
    <text class="t-foot" x="282" y="160">7</text>
  </svg>
  <div class="kicker"></div>
  <div class="title"><b>Annual</b> Revenue</div>
  <div class="sub">Short financial results review.</div>
</div>

<!-- Global presence -->
<div class="slide c1 r3">
  <svg viewBox="0 0 296 166">
    <rect x="60" y="48" width="180" height="90" rx="20" fill="#a8a8a8" role="img" aria-label="World map in grey"/>
    <g fill="var(--blue)" stroke="#fff" stroke-width=".8">
      <circle cx="44" cy="66" r="19"/><circle cx="256" cy="66" r="19"/><circle cx="72" cy="116" r="18"/>
      <circle cx="140" cy="118" r="21"/><circle cx="184" cy="118" r="14"/><circle cx="246" cy="120" r="17"/>
    </g>
    <g text-anchor="middle">
      <text class="t-label-w" x="44" y="64">N. AMERICA</text><text class="t-tiny" x="44" y="69" style="fill:#fff">Short sample text</text>
      <text class="t-label-w" x="256" y="64">ASIA</text><text class="t-tiny" x="256" y="69" style="fill:#fff">Short sample text</text>
      <text class="t-label-w" x="72" y="114">S. AMERICA</text><text class="t-tiny" x="72" y="119" style="fill:#fff">Short sample text</text>
      <text class="t-label-w" x="140" y="116">EUROPE</text><text class="t-tiny" x="140" y="121" style="fill:#fff">Short sample text</text>
      <text class="t-label-w" x="184" y="116">AFRICA</text><text class="t-tiny" x="184" y="121" style="fill:#fff">Short text</text>
      <text class="t-label-w" x="246" y="118">OCEANIA</text><text class="t-tiny" x="246" y="123" style="fill:#fff">Short sample text</text>
    </g>
    <rect y="150" width="296" height="16" fill="#fff"/>
    <text class="brand" x="5" y="161" font-size="5.5">BRIMWOOD CAPITAL</text>
    <polygon points="82,150 296,150 296,166 70,166" fill="var(--blue)"/>
    <polygon points="270,150 296,150 296,166 258,166" fill="var(--blue-light)"/>
    <text class="t-foot" x="232" y="160" text-anchor="end">© Brimwood Capital 2017</text>
    <text class="t-foot" x="282" y="160">9</text>
  </svg>
  <div class="kicker"></div>
  <div class="title"><b>Global</b> Presence</div>
  <div class="sub">Short description for the global presence.</div>
</div>

<!-- Puzzle -->
<div class="slide c2 r3">
  <svg viewBox="0 0 296 166">
    <g transform="translate(148,93) rotate(45)">
      <rect x="-24" y="-24" width="23" height="23" rx="2" fill="var(--blue)"/>
      <rect x="1" y="-24" width="23" height="23" rx="2" fill="var(--grey-dark)"/>
      <rect x="-24" y="1" width="23" height="23" rx="2" fill="var(--grey-dark)"/>
      <rect x="1" y="1" width="23" height="23" rx="2" fill="#a3a3a3"/>
    </g>
    <g stroke="var(--grey-light)" stroke-width=".5" fill="none">
      <polyline points="114,70 130,70 140,76"/><polyline points="114,110 124,110 131,104"/>
      <polyline points="206,86 182,86 170,83"/><polyline points="206,126 176,126 160,116"/>
    </g>
    <g text-anchor="end">
      <text class="t-label" x="110" y="71">MARKETING</text><text class="t-tiny" x="110" y="76">Short sample line of text</text>
      <text class="t-label" x="110" y="111">SEARCH &amp; RESULTS</text><text class="t-tiny" x="110" y="116">Short sample line of text</text>
    </g>
    <text class="t-label" x="210" y="87">KEY ACHIEVEMENTS</text><text class="t-tiny" x="210" y="92">Short sample line of text</text>
    <text class="t-label" x="210" y="127">FIRE AND LAUNCH</text><text class="t-tiny" x="210" y="132">Short sample line of text</text>
    <rect y="150" width="296" height="16" fill="#fff"/>
    <text class="brand" x="5" y="161" font-size="5.5">BRIMWOOD CAPITAL</text>
    <polygon points="82,150 296,150 296,166 70,166" fill="var(--blue)"/>
    <polygon points="270,150 296,150 296,166 258,166" fill="var(--blue-light)"/>
    <text class="t-foot" x="232" y="160" text-anchor="end">© Brimwood Capital 2017</text>
    <text class="t-foot" x="282" y="160">10</text>
  </svg>
  <div class="kicker"></div>
  <div class="title"><b>Infographic</b> Puzzle</div>
  <div class="sub">Short description</div>
</div>

<!-- Process -->
<div class="slide c3 r3">
  <svg viewBox="0 0 296 166">
    <g class="process-band">
      <rect x="60" y="108" width="36" height="8" fill="var(--grey-mid)"/>
      <rect x="96" y="108" width="36" height="8" fill="var(--blue)"/>
      <rect x="132" y="108" width="36" height="8" fill="var(--grey-dark)"/>
      <rect x="168" y="108" width="36" height="8" fill="var(--grey-soft)"/>
      <rect x="204" y="108" width="36" height="8" fill="var(--blue)"/>
    </g>
    <g fill="#fff" stroke-width="1">
      <circle cx="78" cy="112" r="6" stroke="var(--grey-mid)"/>
      <circle cx="114" cy="112" r="6" stroke="var(--blue)"/>
      <circle cx="150" cy="112" r="6" stroke="var(--grey-dark)"/>
      <circle cx="186" cy="112" r="6" stroke="var(--grey-soft)"/>
      <circle cx="222" cy="112" r="6" stroke="var(--blue)"/>
    </g>
    <g fill="none" stroke="var(--grey-dark)" stroke-width=".6">
      <circle cx="78" cy="111" r="2"/><line x1="77" y1="113.5" x2="79" y2="113.5"/>
      <circle cx="113.4" cy="111.4" r="1.8"/><line x1="114.7" y1="112.7" x2="116.4" y2="114.4"/>
      <circle cx="150" cy="112" r="2.2"/><circle cx="150" cy="112" r=".8"/>
      <rect x="183" y="110" width="6" height="4"/>
      <path d="M218.5,110.5 h5 v3 h-5 z M223.5,111.5 h2 l1,1 v1 h-3"/>
    </g>
    <circle cx="54" cy="112" r="1.5" fill="var(--blue)"/><circle cx="246" cy="112" r="1.5" fill="var(--blue)"/>
    <text class="t-label" x="54" y="120" text-anchor="middle">Start</text>
    <text class="t-label" x="246" y="120" text-anchor="middle">Finish</text>
    <g text-anchor="middle" class="t-label" style="fill:var(--grey-dark)">
      <text x="78" y="101">CREATIVE IDEA</text><text x="150" y="101">CONCEPT</text><text x="222" y="101">DELIVERY</text>
      <text x="114" y="126">RESEARCH</text><text x="186" y="126">DESIGN</text>
    </g>
    <g text-anchor="middle">
      <text class="t-tiny" x="78" y="90">Short sample line</text><text class="t-tiny" x="78" y="94">of step text</text>
      <text class="t-tiny" x="150" y="90">Short sample line</text><text class="t-tiny" x="150" y="94">of step text</text>
      <text class="t-tiny" x="222" y="90">Short sample line</text><text class="t-tiny" x="222" y="94">of step text</text>
      <text class="t-tiny" x="114" y="132">Short sample line</text><text class="t-tiny" x="114" y="136">of step text</text>
      <text class="t-tiny" x="186" y="132">Short sample line</text><text class="t-tiny" x="186" y="136">of step text</text>
    </g>
    <rect y="150" width="296" height="16" fill="#fff"/>
    <text class="brand" x="5" y="161" font-size="5.5">BRIMWOOD CAPITAL</text>
    <polygon points="82,150 296,150 296,166 70,166" fill="var(--blue)"/>
    <polygon points="270,150 296,150 296,166 258,166" fill="var(--blue-light)"/>
    <text class="t-foot" x="232" y="160" text-anchor="end">© Brimwood Capital 2017</text>
    <text class="t-foot" x="282" y="160">11</text>
  </svg>
  <div class="kicker"></div>
  <div class="title"><b>Services</b> Process</div>
  <div class="sub">Short description</div>
</div>

<!-- Closing -->
<div class="slide c4 r3">
  <svg viewBox="0 0 296 166">
    <rect class="photo-sky" width="296" height="166" role="img" aria-label="City skyline photo with cable-stayed bridge at dusk"/>
    <polygon points="296,20 296,166 170,166" fill="#fff" opacity=".85"/>
    <text class="t-big" x="8" y="134" font-size="12">Thank you for your time</text>
    <text class="brand" x="288" y="157" font-size="8" text-anchor="end">BRIMWOOD CAPITAL</text>
  </svg>
</div>
</body>
</html>
```